I am a business consultant/coach and I am branding myself 'The Free Rein Trade Mentor'. My business name is Bright Harbour Advisory.I want an oversized postcard designed for lead generation. It will be sent through the post so will require area for an address and stamp The details that I want on the card are attached plus a photo of myself. Also I have attached a copy of my business card so that you are able to see the style and colors I use. I would like the main headline to be bold red, or bold red background Hope this is enough info.
Target Market(s)
Owners/managers of medium sized businesses
Industry/Entity Type
Business Consultant
Requirements
Must have
- The cards I want to be noticed and professional in appearance, they will be use dfor lead generation and sent through the postal service
Nice to have
- The colors that I use on my business cards are green, grey and white. I want the main headline to be in red or red backgroun dso that it stands out
Should not have
- The words that I have used are basically off my landing page for consistency

```html
<!DOCTYPE html>
<html lang="en">
<head>
<meta charset="utf-8">
<title>Bright Harbour Advisory – Lead Generation Postcard</title>
<link href="https://fonts.googleapis.com/css2?family=Oswald:wght@500;600;700&family=Lato:wght@400;700;900&display=swap" rel="stylesheet">
<style>
:root{
  --red:#e8303a;
  --green:#9bc63b;
  --grey-dark:#3a3a3c;
  --grey-mid:#8d8e90;
  --grey-light:#d9d9da;
  --ink:#222;
  --white:#fff;
  --page:#ecebe8;
  --line:#c7c7c7;
  --stamp:#e3e3e3;
}
*{box-sizing:border-box;margin:0;padding:0}
html,body{width:900px;height:1200px;overflow:hidden;background:var(--page)}
body{position:relative;font-family:'Lato',sans-serif;color:var(--ink)}
.card{position:absolute;left:40px;width:820px;height:540px;background:var(--white);overflow:hidden;box-shadow:0 4px 14px rgba(0,0,0,.18)}
.card--front{top:40px}
.card--back{top:620px}

/* FRONT */
.headline-band{position:absolute;left:232px;top:0;width:588px;height:152px;background:var(--red);padding:26px 20px 0 24px}
.headline{font-family:'Oswald',sans-serif;font-weight:600;font-size:40px;line-height:1.1;text-transform:uppercase;color:var(--white)}
.headline .dark{color:var(--grey-dark)}
.brand-name{position:absolute;left:40px;top:140px;height:40px;font-weight:900;font-size:30px;line-height:40px;color:var(--grey-dark);display:flex;align-items:center;gap:8px}
.brand-name .dot{width:12px;height:12px;background:var(--green);border-radius:50%}
.promise-band{position:absolute;left:0;top:196px;width:560px;height:56px;background:var(--green);clip-path:polygon(0 0,100% 0,94% 100%,0 100%);padding:9px 0 0 40px;font-family:'Oswald',sans-serif;font-weight:600;font-size:26px;color:var(--white);text-transform:uppercase}
.intro{position:absolute;left:50px;top:282px;width:490px;font-size:21px;font-weight:700;line-height:1.3;color:var(--ink);transform:rotate(-3deg);transform-origin:left top}
.research-pill{position:absolute;left:40px;top:374px;width:440px;height:56px;border-radius:28px;background:linear-gradient(#f2f2f2,var(--grey-light));display:flex;align-items:center;padding-left:28px;font-weight:700;font-size:25px;color:var(--red)}
.portrait{position:absolute;left:560px;top:152px;width:260px;height:268px;background:linear-gradient(160deg,#c9ccd0,#e8d3c3 55%,#f4f4f4)}
.base-strip{position:absolute;left:0;top:490px;width:820px;height:50px;background:linear-gradient(var(--grey-mid),var(--grey-dark))}
.call-band{position:absolute;left:0;top:440px;width:500px;height:72px;background:var(--green);display:flex;align-items:center;gap:12px;padding-left:40px;color:var(--white);font-family:'Oswald',sans-serif;font-weight:600;z-index:1}
.call-band .label{font-size:28px}
.call-band .number{font-size:44px;color:var(--grey-dark)}
.name-panel{position:absolute;left:470px;top:420px;width:350px;height:70px;background:linear-gradient(#e6e6e6,#b9babc);clip-path:polygon(8% 0,100% 0,100% 100%,0 100%);padding:9px 14px 0 50px;text-align:right;font-weight:700;font-size:15px;line-height:1.3;color:var(--ink);z-index:1}
.name-panel .accent{color:var(--red)}

/* BACK */
.back-copy{position:absolute;left:0;top:20px;width:370px;height:510px}
.section-title{font-family:'Oswald',sans-serif;font-weight:600;font-size:19px;line-height:1.2;text-transform:uppercase;display:block}
.section-because{height:128px;background:var(--red);padding:12px 18px;color:var(--white);font-size:15px;line-height:1.3}
.section-problem{height:124px;background:var(--green);padding:10px 18px;color:var(--ink);font-size:14px;line-height:1.3}
.section-problem .section-title{color:var(--grey-dark)}
.section-offer{height:108px;padding:10px 18px;font-size:14.5px;line-height:1.35}
.section-promise{position:relative;height:150px;background:var(--grey-dark);color:var(--white)}
.promise-text{position:absolute;left:18px;top:8px;width:222px;font-size:11px;line-height:1.35}
.promise-text .section-title{color:var(--green);font-size:17px}
.more-info{position:absolute;left:0;top:76px;width:240px;height:20px;background:var(--green);font-size:11px;font-weight:700;padding:3px 0 0 18px;color:var(--ink)}
.contacts{position:absolute;left:18px;top:100px;width:230px;list-style:none;color:var(--white);font-size:11px;line-height:1.5}
.contacts li{display:flex;align-items:center;gap:8px}
.contacts svg{width:10px;height:10px;flex:none}
.promise-portrait{position:absolute;right:6px;top:0;width:118px;height:150px;background:linear-gradient(160deg,#c9ccd0,#e8d3c3 55%,#f4f4f4)}
.divider{position:absolute;left:372px;top:20px;width:14px;height:510px;background:var(--grey-dark);border-right:4px solid var(--green)}
.stamp-box{position:absolute;left:610px;top:40px;width:150px;height:140px;background:var(--stamp)}
.address-line{position:absolute;left:430px;width:340px;height:2px;background:var(--line)}
.address-line--1{top:240px}
.address-line--2{top:310px}
.address-line--3{top:380px}
</style>
</head>
<body>

<section class="card card--front">
  <div class="headline-band">
    <h1 class="headline">Has your business achieved<br><span class="dark">the outcomes you want?</span></h1>
  </div>
  <div class="brand-name"><span>brightharbour</span><span class="dot"></span></div>
  <div class="promise-band">It can and I'm prepared to show you how</div>
  <p class="intro">If I told you that you can increase your profits, give yourself more time, freedom and peace, what would your answer be…?</p>
  <div class="research-pill">Research says you can and quickly</div>
  <div class="portrait" role="img" aria-label="Head-and-shoulders portrait of the business mentor, smiling"></div>
  <div class="base-strip"></div>
  <div class="call-band"><span class="label">Call me on</span><span class="number">0412000345</span></div>
  <div class="name-panel">My name is DANIEL HARLOW<br><span class="accent">from Bright Harbour Advisory,<br>the 'Free Rein Trade Mentor'.</span></div>
</section>

<section class="card card--back">
  <div class="back-copy">
    <div class="section-because">
      <span class="section-title">Because</span>
      Over 90 percent of small to medium sized business in Australia have a minimum of 12 per cent of their annual turnover tied up in ineffective and inefficient processes?
    </div>
    <div class="section-problem">
      <span class="section-title">The problem is that</span>
      Most business owners focus on their daily challenges unable to free themselves to consider where the 'hidden profit' may be locked up within their business.
    </div>
    <div class="section-offer">
      I can change this by reviewing your cashflow, systems, staff capability, business culture and Risk. The end result will be more money, time, freedom and peace to live your life that way you desire.
    </div>
    <div class="section-promise">
      <div class="promise-text">
        <span class="section-title">My promise:</span>
        If I cannot uncover at least 5 times my fee from potential profits hidden with your business after one interview then it is free.
      </div>
      <div class="more-info">If you would like more information go to</div>
      <ul class="contacts">
        <li><svg viewBox="0 0 10 10"><circle cx="5" cy="5" r="4" fill="none" stroke="#9bc63b" stroke-width="1.5"/></svg>www.brightharbour.example/freerein</li>
        <li><svg viewBox="0 0 10 10"><rect x="1" y="2" width="8" height="6" fill="none" stroke="#9bc63b" stroke-width="1.3"/><path d="M1 2l4 3 4-3" fill="none" stroke="#9bc63b" stroke-width="1.3"/></svg>email hello@brightharbour.example</li>
        <li><svg viewBox="0 0 10 10"><path d="M2 1h2l1 2-1.2 1a5 5 0 0 0 2.2 2.2L7 5l2 1v2c-4 .5-8-3.5-7-7z" fill="#9bc63b"/></svg>0412000345</li>
      </ul>
      <div class="promise-portrait" role="img" aria-label="Small portrait of the business mentor"></div>
    </div>
  </div>
  <div class="divider"></div>
  <div class="stamp-box"></div>
  <div class="address-line address-line--1"></div>
  <div class="address-line address-line--2"></div>
  <div class="address-line address-line--3"></div>
</section>

</body>
</html>
```